Township of Quenford E-Alert Signup

Need to create print media that is designed for a Town in New Jersey that is starting a marketing campaign to get townspeople to sign up for the E-Alert system.Need print media that is 1. interchangeable in size (regular letter-size, as well as a poster size) 2. Branded with their colors, logo, etc. (green and white displayed in logo)3. Displays the incentives to sign up. Incentives:- Community Services/Announcements- Gov’t/Non-profit Resources- Tax Information- Employment opportunities- Municipal Services/Public Works/Recreation Divisions- Health Updates
Target Market(s)
Townspeople of Maplewood NJ
Industry/Entity Type
Government
Colors
Designer to choose colors to be used in the design.
Requirements
Must have
- 1. interchangeable in size (regular letter-size, as well as a poster size)
- 2. Branded with their colors, logo, etc. (green and white displayed in logo)
- 3. Displays the incentives to sign up.
- Incentives:
- - Community Services/Announcements
- - Gov’t/Non-profit Resources
- - Tax Information
- - Employment opportunities
- - Municipal Services/Public Works/Recreation Divisions
- - Health Updates

```html
<!DOCTYPE html>
<html lang="en">
<head>
<meta charset="utf-8">
<title>Township of Quenford E-Alert Flyer</title>
<link href="https://fonts.googleapis.com/css2?family=Tinos:wght@400;700&family=Oswald:wght@500;600&family=Montserrat:wght@500;600&display=swap" rel="stylesheet">
<style>
  :root {
    --green-dark: #1f5a2a;
    --green: #2b6b33;
    --green-icon: #2f7a3a;
    --cream: #f3eed9;
    --cream-light: #faf7ea;
    --ink: #1c1c1c;
    --white: #ffffff;
    --backdrop: #e9e9e6;
  }
  * { box-sizing: border-box; margin: 0; padding: 0; }
  html, body { width: 1024px; height: 1200px; overflow: hidden; background: var(--backdrop); }
  .flyer {
    position: absolute; left: 62px; top: 18px; width: 900px; height: 1164px;
    background: var(--white); overflow: hidden;
    box-shadow: 0 2px 10px rgba(0,0,0,.15);
  }
  .header { position: absolute; left: 0; top: 0; width: 520px; height: 160px; padding: 28px 0 0 38px; }
  .header__kicker { font-family: "Tinos", serif; font-size: 33px; color: var(--ink); line-height: 1; }
  .header__title { font-family: "Tinos", serif; font-weight: 700; font-size: 52px; color: var(--green-dark); line-height: 1.1; margin-top: 6px; }
  .photo { position: absolute; }
  .photo--creek { left: 0; top: 164px; width: 253px; height: 206px; background: linear-gradient(160deg, #c9a25a, #7a8a4a 45%, #4f6a44 75%, #8d9a9a); }
  .photo--firehouse { left: 261px; top: 164px; width: 252px; height: 206px; background: linear-gradient(180deg, #9cc3ea 0 30%, #8a3a2c 30%, #6e2e24 75%, #555 75%); }
  .photo--hall { left: 0; top: 380px; width: 253px; height: 210px; background: linear-gradient(180deg, #27405f 0 30%, #7a4a3a 30%, #c9b39a 65%, #2f3138 65%); }
  .photo--crosswalk { left: 261px; top: 380px; width: 252px; height: 210px; background: radial-gradient(circle at 50% 55%, #6a6d70 0 30%, #3f6a36 55%, #2d5028); }
  .photo--street { left: 520px; top: 0; width: 380px; height: 590px; background: linear-gradient(180deg, #3d78c8 0 25%, #5d7a55 38%, #a89a86 55%, #6b6b6b 80%, #5a5a5a); }
  .lower {
    position: absolute; left: 0; top: 590px; width: 900px; height: 487px;
    background: linear-gradient(180deg, var(--cream) 0%, var(--cream-light) 55%, #efe9d3 100%);
  }
  .seal {
    position: absolute; left: 624px; top: 483px; width: 250px; height: 250px; border-radius: 50%;
    background: var(--white); border: 5px solid var(--green);
    display: flex; align-items: center; justify-content: center; text-align: center;
    font-family: "Montserrat", sans-serif; font-weight: 600; font-size: 24px; line-height: 1.25; color: var(--green);
    padding: 30px;
  }
  .headline {
    position: absolute; left: 37px; top: 626px; width: 580px;
    font-family: "Oswald", sans-serif; font-weight: 600; font-size: 31px; line-height: 44px;
    color: var(--green-dark); text-transform: uppercase;
  }
  .incentives__label {
    position: absolute; left: 37px; top: 736px; line-height: 36px;
    font-family: "Oswald", sans-serif; font-weight: 600; font-size: 27px; color: var(--green-dark);
  }
  .incentive { position: absolute; display: flex; align-items: center; gap: 14px; height: 66px; }
  .incentive--left { left: 42px; }
  .incentive--right { left: 450px; }
  .incentive--row1 { top: 782px; }
  .incentive--row2 { top: 860px; }
  .incentive--row3 { top: 943px; }
  .incentive__icon {
    width: 66px; height: 66px; border-radius: 50%; background: var(--green-icon);
    border: 4px solid var(--white); box-shadow: 0 1px 4px rgba(0,0,0,.35);
    display: flex; align-items: center; justify-content: center; flex: none;
  }
  .incentive__icon svg { width: 36px; height: 36px; }
  .incentive__text { font-family: "Montserrat", sans-serif; font-weight: 600; font-size: 20px; line-height: 1.2; color: var(--ink); }
  .footer { position: absolute; left: 0; top: 1077px; width: 900px; height: 87px; background: var(--green-dark); }
  .footer__url {
    position: absolute; left: 254px; top: -18px; width: 392px; height: 48px; border-radius: 24px;
    background: var(--green); box-shadow: 0 2px 6px rgba(0,0,0,.3);
    display: flex; align-items: center; justify-content: center; gap: 10px;
    font-family: "Montserrat", sans-serif; font-weight: 600; font-size: 22px; color: var(--white);
  }
  .footer__contact {
    position: absolute; left: 0; right: 0; top: 42px; text-align: center;
    font-family: "Montserrat", sans-serif; font-weight: 500; font-size: 18px; color: var(--white);
  }
</style>
</head>
<body>
<div class="flyer">
  <div class="header">
    <p class="header__kicker">Help Us Help You</p>
    <h1 class="header__title">E-Alert system</h1>
  </div>

  <div class="photo photo--creek" role="img" aria-label="Autumn creek winding through a park"></div>
  <div class="photo photo--firehouse" role="img" aria-label="Brick firehouse with a ladder truck"></div>
  <div class="photo photo--hall" role="img" aria-label="Municipal building lit at dusk"></div>
  <div class="photo photo--crosswalk" role="img" aria-label="Aerial view of a rainbow crosswalk"></div>
  <div class="photo photo--street" role="img" aria-label="Downtown street with shops and parked cars"></div>

  <div class="lower" role="img" aria-label="Faded view of the town centre"></div>

  <div class="seal">Township of Quenford</div>

  <h2 class="headline">Get the most up to date local news and<br>information with our free e-alerts</h2>

  <h3 class="incentives__label">INCENTIVES:</h3>

  <div class="incentive incentive--left incentive--row1">
    <span class="incentive__icon"><svg viewBox="0 0 24 24" fill="#fff"><path d="M3 9h4l5-4v14l-5-4H3z"/><path d="M15 8.5a5 5 0 0 1 0 7M17.5 6a8.5 8.5 0 0 1 0 12" fill="none" stroke="#fff" stroke-width="1.8" stroke-linecap="round"/></svg></span>
    <span class="incentive__text">Community Services/<br>Announcements</span>
  </div>
  <div class="incentive incentive--left incentive--row2">
    <span class="incentive__icon"><svg viewBox="0 0 24 24" fill="#fff"><path d="M12 2 2 7v2h20V7z"/><rect x="4" y="10" width="2.5" height="8"/><rect x="8.5" y="10" width="2.5" height="8"/><rect x="13" y="10" width="2.5" height="8"/><rect x="17.5" y="10" width="2.5" height="8"/><rect x="2" y="19" width="20" height="3"/></svg></span>
    <span class="incentive__text">Gov’t/Non-profit Resources</span>
  </div>
  <div class="incentive incentive--left incentive--row3">
    <span class="incentive__icon"><svg viewBox="0 0 24 24" fill="#fff"><rect x="3" y="15" width="3" height="6"/><rect x="8" y="12" width="3" height="9"/><rect x="13" y="9" width="3" height="12"/><rect x="18" y="6" width="3" height="15"/><path d="M3 11 9 6l4 3 7-6" fill="none" stroke="#fff" stroke-width="1.6"/></svg></span>
    <span class="incentive__text">Tax Information</span>
  </div>

  <div class="incentive incentive--right incentive--row1">
    <span class="incentive__icon"><svg viewBox="0 0 24 24" fill="#fff"><circle cx="12" cy="7" r="3"/><circle cx="5" cy="9" r="2.3"/><circle cx="19" cy="9" r="2.3"/><path d="M6.5 19a5.5 5.5 0 0 1 11 0z"/><path d="M1 19a4 4 0 0 1 6-3.5V19zM23 19a4 4 0 0 0-6-3.5V19z"/></svg></span>
    <span class="incentive__text">Employment opportunities</span>
  </div>
  <div class="incentive incentive--right incentive--row2">
    <span class="incentive__icon"><svg viewBox="0 0 24 24" fill="none" stroke="#fff" stroke-width="2.4"><circle cx="9" cy="14" r="4.5" stroke-dasharray="2.4 1.4"/><circle cx="9" cy="14" r="1.5" fill="#fff"/><circle cx="17" cy="7" r="3.5" stroke-dasharray="2 1.2"/></svg></span>
    <span class="incentive__text">Municipal Services/<br>Public Works/Recreation Divisions</span>
  </div>
  <div class="incentive incentive--right incentive--row3">
    <span class="incentive__icon"><svg viewBox="0 0 24 24" fill="#fff"><rect x="10" y="4" width="4" height="16"/><rect x="4" y="10" width="16" height="4"/></svg></span>
    <span class="incentive__text">Health Updates</span>
  </div>

  <div class="footer">
    <div class="footer__url">
      <svg width="22" height="22" viewBox="0 0 24 24" fill="none" stroke="#fff" stroke-width="2"><circle cx="12" cy="12" r="9"/><path d="M3 12h18M12 3c3 3 3 15 0 18M12 3c-3 3-3 15 0 18"/></svg>
      www.twp.quenford.nj.us
    </div>
    <p class="footer__contact">210 Linden Ave., Quenford Township, NJ 07950 &nbsp;|&nbsp; Ph: (555) 014-2290</p>
  </div>
</div>
</body>
</html>
```